Information One Page for Email

I am looking for a informative attachment I can send with an introductive email for Maplecrest Slab Works. Something I can also Mail.

Maplecrest Slab Works is the leader in Rebar Post Tension Cable Placement and Post Tension Cable repair. Outside of cable placement and repair we do concrete repair, Parking Garage restoration and

Content

Post Tension Repair and Concrete Restoration
Post-tensioning is a revolutionary method in concrete construction that enhances the strength and durability of structures. However, like all construction ele-ments, post-tension cables can experience wear and damage over time. Ensuring timely and effective repair is crucial for maintaining the safety and integrity of your building.
Why Post-Tension Cable Repair is Essential
1. **Structural Integrity**: Damaged or deteriorated cables can compromise the structural integrity of your building, leading to safety hazards and potential structural failures.
2. **Extended Lifespan**: Regular maintenance and repair of post-tension cables extend the lifespan of your structure, ensuring it remains safe and function-al for years to come.
3. **Cost-Effective**: Addressing cable issues early on prevents more severe damage and costly repairs down the line.
Common Signs of Post-Tension Cable Issues
- Cracks in concrete surfaces
- Unusual noises or popping sounds
- Visible cable ends or broken strands
- Water leakage through cracks
Our Repair Process
1. **Inspection and Assessment**: Our team conducts a thorough inspection to identify the extent of the damage and determine the appropriate repair meth-ods.
2. **Cable Repair or Replacement**: Depending on the severity, we either re-pair the existing cables or replace them with new ones to restore full functional-ity.
3. **Sealing and Protection**: After repairing, we seal the affected areas to protect against moisture and future damage.
4. **Quality Assurance**: We perform rigorous quality checks to ensure the repairs meet industry standards and the structure is safe for use.
Why Choose Us
- **Expertise and Experience**: With years of experience in post-tension cable repair, our team is skilled in handling even the most complex repairs efficiently and effectively.
- **Advanced Technology**: We use the latest technology and materials to ensure durable and long-lasting repairs.
- **Customer Satisfaction**: Our commitment to quality and customer satisfaction sets us apart. We work closely with our clients to ensure their needs are met and expectations exceeded.
Contact Us
If you suspect issues with your post-tension cables or need a routine inspection, don't hesitate to contact us. Our experts are ready to provide the best solutions to keep your structures safe and secure.
Ensure the safety and longevity of your building with our professional post-tension cable repair services. Trust us to deliver quality and reliability every time.

```html
<!DOCTYPE html>
<html lang="en">
<head>
<meta charset="utf-8">
<title>Maplecrest Slab Works – Post-Tension Repair</title>
<link href="https://fonts.googleapis.com/css2?family=Montserrat:wght@600;700&family=Inter:wght@400;600&display=swap" rel="stylesheet">
<style>
:root{
  --green:#136b35;
  --gray-panel:#707073;
  --backdrop:#bdbdbd;
  --ink:#1c1c1c;
  --white:#ffffff;
  --black:#0d0d0d;
  --photo-a:#c9c6bf;
  --photo-b:#8e8b85;
}
*{margin:0;padding:0;box-sizing:border-box}
html,body{width:960px;height:1200px;overflow:hidden;background:var(--backdrop)}
body{font-family:"Inter",sans-serif;color:var(--ink)}
.sheet{position:absolute;left:133px;top:110px;width:694px;height:981px;background:var(--white);overflow:hidden}
.brand{position:absolute;left:40px;top:48px;display:flex;align-items:center;gap:8px;font-family:"Montserrat",sans-serif;font-weight:700;font-size:17px;color:var(--green)}
.brand-dot{width:12px;height:12px;background:var(--green)}
.hero-band{position:absolute;left:0;top:118px;width:480px;height:156px;background:var(--green)}
.hero-photo{position:absolute;left:334px;top:0;width:360px;height:274px;background:linear-gradient(135deg,var(--photo-a),var(--photo-b));clip-path:polygon(32% 0,100% 0,100% 100%,0 100%,18% 72%,36% 40%,44% 22%)}
.hero-title{position:absolute;left:40px;top:132px;width:300px;font-family:"Montserrat",sans-serif;font-weight:700;font-size:20px;line-height:24px;color:var(--white)}
.hero-intro{position:absolute;left:40px;top:184px;width:290px;font-size:10px;line-height:12.3px;color:var(--white)}
.section-title{position:absolute;font-family:"Montserrat",sans-serif;font-weight:700;font-size:14.3px;line-height:17px;color:var(--green)}
.item{position:absolute;display:flex;gap:0}
.item-icon{position:absolute;left:0;top:2px;width:32px;height:32px}
.item-body{position:absolute;left:47px;top:0;font-size:10px;line-height:12.6px}
.item-body strong{display:block;font-weight:600}
.signs{position:absolute;left:48px;top:608px;list-style:none;font-size:10px}
.signs li{height:21px;display:flex;align-items:center;gap:7px}
.signs li::before{content:"";width:4.5px;height:4.5px;border-radius:50%;background:var(--ink)}
.site-photo{position:absolute;left:40px;top:697px;width:279px;height:133px;border-radius:10px;background:linear-gradient(180deg,#b7b9bb,#8f908e 60%,#6f6e6a)}
.process-panel{position:absolute;left:347px;top:274px;width:316px;height:558px;background:var(--gray-panel);border-radius:0 0 22px 22px;color:var(--white)}
.process-panel .section-title{color:var(--white)}
.process-panel .item-body{left:63px;width:235px}
.process-panel .item-icon{left:20px}
.contact-band{position:absolute;left:0;top:844px;width:694px;height:137px;background:var(--green);color:var(--white);text-align:center;font-size:10px;line-height:12.6px}
.contact-tab{position:absolute;left:280px;top:0;width:133px;height:26px;background:var(--black);clip-path:polygon(0 0,100% 0,90% 100%,10% 100%);font-family:"Montserrat",sans-serif;font-weight:700;font-size:13.5px;line-height:26px}
.contact-line{position:absolute;left:0;width:100%}
.contact-bar{position:absolute;left:35px;top:90px;width:624px;height:29px;border:1px dashed rgba(255,255,255,.45);border-radius:15px;display:flex;align-items:center;font-size:11.5px}
.contact-bar span{display:flex;align-items:center;gap:8px;justify-content:center}
.contact-bar .divider{width:1px;height:18px;background:rgba(255,255,255,.5)}
.contact-bar svg{width:15px;height:15px}
</style>
</head>
<body>
<svg width="0" height="0" style="position:absolute">
  <defs>
    <symbol id="idea-gear" viewBox="0 0 32 32">
      <g fill="none" stroke="currentColor" stroke-width="1.4" stroke-linecap="round">
        <path d="M10 20c-3-2-4-5-4-8a8 8 0 0 1 16 0c0 3-1 5-3 7v4h-9z"/>
        <path d="M11 26h7M12 29h5"/>
        <circle cx="20" cy="10" r="3.5"/>
        <path d="M20 4v2M20 14v2M14 10h2M24 10h2"/>
        <path d="M2 6l3 2M2 14h3M28 22l-2-2M28 26h-3"/>
      </g>
    </symbol>
  </defs>
</svg>
<div class="sheet">
  <div class="brand"><span class="brand-dot"></span>Maplecrest Slab Works</div>

  <div class="hero-band"></div>
  <div class="hero-photo" role="img" aria-label="Photo of a concrete building facade under post-tension balcony repair with shoring"></div>
  <h1 class="hero-title">Post-Tension Repair and Concrete Restoration</h1>
  <p class="hero-intro">Post-tensioning is a revolutionary method in concrete construction that enhances the strength and durability of structures. However, like all construction ele-ments, post-tension cables can experience wear and damage over time. Ensuring timely and effective repair is crucial for maintaining the safety and integrity of your building.</p>

  <h2 class="section-title" style="left:40px;top:299px">Why Post-Tension<br>Cable Repair Is Essential</h2>

  <div class="item" style="left:40px;top:350px;color:var(--green)">
    <svg class="item-icon"><use href="#idea-gear"/></svg>
    <p class="item-body" style="width:225px;color:var(--ink)"><strong>Structural Integrity</strong>Damaged or deteriorated cables can compromise the structural integrity of your building, leading to safety hazards and potential structural failures.</p>
  </div>
  <div class="item" style="left:40px;top:426px;color:var(--green)">
    <svg class="item-icon"><use href="#idea-gear"/></svg>
    <p class="item-body" style="width:225px;color:var(--ink)"><strong>Extended Lifespan</strong>Regular maintenance and repair of post-tension cables extend the lifespan of your structure, ensuring it remains safe and functional for years to come.</p>
  </div>
  <div class="item" style="left:40px;top:501px;color:var(--green)">
    <svg class="item-icon"><use href="#idea-gear"/></svg>
    <p class="item-body" style="width:225px;color:var(--ink)"><strong>Cost-Effective</strong>Addressing cable issues early prevents more severe damage and costly repairs down the line.</p>
  </div>

  <h2 class="section-title" style="left:40px;top:562px">Common Signs of<br>Post-Tension Cable Issues</h2>
  <ul class="signs">
    <li>Cracks in concrete surfaces</li>
    <li>Unusual noises or popping sounds</li>
    <li>Visible cable ends or broken strands</li>
    <li>Water leakage through cracks</li>
  </ul>
  <div class="site-photo" role="img" aria-label="Photo of a parking garage deck beside high-rise condominium towers"></div>

  <section class="process-panel">
    <h2 class="section-title" style="left:20px;top:18px">Our Repair Process</h2>
    <div class="item" style="left:0;top:53px">
      <svg class="item-icon"><use href="#idea-gear"/></svg>
      <p class="item-body"><strong>Inspection and Assessment</strong>Our team conducts a thorough inspection to identify the extent of the damage and determine the appropriate repair methods.</p>
    </div>
    <div class="item" style="left:0;top:116px">
      <svg class="item-icon"><use href="#idea-gear"/></svg>
      <p class="item-body"><strong>Cable Repair or Replacement</strong>Depending on the severity, we either repair the existing cables or replace them with new ones to restore full functionality.</p>
    </div>
    <div class="item" style="left:0;top:179px">
      <svg class="item-icon"><use href="#idea-gear"/></svg>
      <p class="item-body"><strong>Sealing and Protection</strong>After repairs are completed, we seal the affected areas to protect against moisture and future damage.</p>
    </div>
    <div class="item" style="left:0;top:242px">
      <svg class="item-icon"><use href="#idea-gear"/></svg>
      <p class="item-body"><strong>Quality Assurance</strong>We perform rigorous quality checks to ensure all repairs meet industry standards and that the structure is safe for continued use.</p>
    </div>

    <h2 class="section-title" style="left:20px;top:316px">Why Choose Maplecrest Slab Works</h2>
    <div class="item" style="left:0;top:352px">
      <svg class="item-icon"><use href="#idea-gear"/></svg>
      <p class="item-body"><strong>Expertise and Experience</strong>With years of experience in post-tension cable repair, our team is equipped to handle even the most complex repairs efficiently and safely.</p>
    </div>
    <div class="item" style="left:0;top:428px">
      <svg class="item-icon"><use href="#idea-gear"/></svg>
      <p class="item-body"><strong>Advanced Technology</strong>We use the latest tools, materials, and methods to ensure durable, long-lasting results.</p>
    </div>
    <div class="item" style="left:0;top:491px">
      <svg class="item-icon"><use href="#idea-gear"/></svg>
      <p class="item-body"><strong>Customer Satisfaction</strong>We work closely with our clients to make sure every project meets expectations and is completed to the highest standard.</p>
    </div>
  </section>

  <footer class="contact-band">
    <div class="contact-tab">Contact Us</div>
    <p class="contact-line" style="top:36px">If you suspect issues with your post-tension cables or need a routine inspection, our experts are ready to help.</p>
    <p class="contact-line" style="top:57px">Ensure the safety and longevity of your building with professional post-tension cable repair services you can trust.<br>Maplecrest Slab Works delivers quality and reliability every time.</p>
    <div class="contact-bar">
      <span style="width:147px"><svg viewBox="0 0 24 24" fill="none" stroke="currentColor" stroke-width="1.5"><path d="M5 3h4l2 5-2.5 1.5a11 11 0 0 0 6 6L16 13l5 2v4a2 2 0 0 1-2 2A17 17 0 0 1 3 5a2 2 0 0 1 2-2z"/></svg>(555) 014-2290</span>
      <span class="divider"></span>
      <span style="width:244px"><svg viewBox="0 0 24 24" fill="none" stroke="currentColor" stroke-width="1.5"><rect x="3" y="6" width="18" height="13" rx="1"/><path d="M3 7l9 7 9-7"/></svg>info@maplecrestslabworks.com</span>
      <span class="divider"></span>
      <span style="width:231px"><svg viewBox="0 0 24 24" fill="none" stroke="currentColor" stroke-width="1.5"><circle cx="12" cy="12" r="9"/><path d="M3 12h18M12 3c3 3 3 15 0 18M12 3c-3 3-3 15 0 18"/></svg>www.maplecrestslabworks.com</span>
    </div>
  </footer>
</div>
</body>
</html>
```